Cover-Design für ein Buch zum Thema Naturheilkunde, Gesundheit und Ernährung
Zielgruppe
In diesem Buch (Ratgeber) werden Möglichkeiten aufgezeigt, die die Naturheilkunde zur Selbstheilung bietet. Gesundheit und Ernährung, so wie eine bewusste Einstellung sind dabei im Vordergrund.
Titel möglicherweise : Heimweg zum Quell der Wiesen
Aufgabenstellung
Ein Design im Bilde der Natur, durch aufzeigen von Landschaft, Sonne, Wasser, Gemüse, Obst, ein Mensch mit ausgestreckten Armen der die Gesundheit und Freiheit symbolisiert. Symboliken wie die Blume des Lebens, das dritte Auge, Kronen chakra, Yin Yang.....

```html
<!DOCTYPE html>
<html lang="de">
<head>
<meta charset="utf-8">
<title>Heimweg zum Quell der Wiesen – Buchcover</title>
<link rel="stylesheet" href="https://fonts.googleapis.com/css2?family=Marcellus&family=Tinos&display=swap">
<style>
  :root {
    --leaf-light: #7fd36a;
    --leaf-mid: #2f9a2c;
    --leaf-deep: #146b18;
    --leaf-dark: #053a08;
    --leaf-night: #011a03;
    --glow: #ffffff;
    --title-white: #ffffff;
    --author-green: #0b4a0e;
    --subtitle-grey: #c9c9c9;
    --emblem-line: #d8d8d8;
  }
  html, body {
    margin: 0;
    padding: 0;
    width: 851px;
    height: 1200px;
    overflow: hidden;
    background: var(--leaf-night);
  }
  .cover {
    position: relative;
    width: 851px;
    height: 1200px;
    overflow: hidden;
  }
  .cover-backdrop {
    position: absolute;
    inset: 0;
    background:
      radial-gradient(ellipse 180px 90px at 415px 0px, var(--glow) 0%, rgba(255,255,255,0.85) 40%, rgba(255,255,255,0) 100%),
      radial-gradient(ellipse 420px 300px at 415px 40px, rgba(220,255,210,0.75) 0%, rgba(160,230,140,0.25) 55%, rgba(0,0,0,0) 100%),
      linear-gradient(90deg, rgba(0,0,0,0) 405px, rgba(170,240,120,0.45) 415px, rgba(170,240,120,0.45) 428px, rgba(0,0,0,0) 440px),
      linear-gradient(180deg, var(--leaf-light) 0%, var(--leaf-mid) 25%, var(--leaf-deep) 55%, var(--leaf-dark) 80%, var(--leaf-night) 100%);
  }
  .author {
    position: absolute;
    left: 504px;
    top: 146px;
    margin: 0;
    font-family: "Marcellus", serif;
    font-size: 40px;
    font-weight: 400;
    color: var(--author-green);
    white-space: nowrap;
  }
  .title {
    margin: 0;
    font-family: "Marcellus", serif;
    font-weight: 400;
    color: var(--title-white);
  }
  .title-part {
    position: absolute;
    white-space: nowrap;
    line-height: 1;
  }
  .title-part--lead { left: 79px; top: 397px; font-size: 50px; }
  .title-part--key { left: 450px; top: 432px; font-size: 88px; }
  .title-part--link { left: 476px; top: 556px; font-size: 44px; }
  .title-part--end { left: 112px; top: 634px; font-size: 84px; }
  .subtitle {
    position: absolute;
    left: 72px;
    top: 968px;
    margin: 0;
    font-family: "Tinos", serif;
    font-size: 38px;
    line-height: 58px;
    color: var(--subtitle-grey);
    width: 420px;
  }
  .emblem {
    position: absolute;
    left: 533px;
    top: 886px;
    width: 240px;
    height: 240px;
  }
</style>
</head>
<body>
  <main class="cover">
    <div class="cover-backdrop" role="img" aria-label="Nahaufnahme eines grünen Blattes mit Wassertropfen und hellem Lichtschein von oben"></div>

    <p class="author">Autor Name</p>

    <h1 class="title">
      <span class="title-part title-part--lead">Heimweg zum</span>
      <span class="title-part title-part--key">Quell</span>
      <span class="title-part title-part--link">der</span>
      <span class="title-part title-part--end">Wiesen</span>
    </h1>

    <p class="subtitle">Ein Ratgeber text text text text text text text</p>

    <svg class="emblem" viewBox="0 0 240 240" role="img" aria-label="Symbol der Blume des Lebens">
      <defs>
        <radialGradient id="emblem-fill" cx="50%" cy="50%" r="50%">
          <stop offset="0%" stop-color="#ffffff" stop-opacity="0.22"/>
          <stop offset="100%" stop-color="#ffffff" stop-opacity="0.08"/>
        </radialGradient>
      </defs>
      <circle cx="120" cy="120" r="118" fill="url(#emblem-fill)" stroke="var(--emblem-line)" stroke-width="2"/>
    </svg>
  </main>
</body>
</html>
```